New Company Business Card Design

I have a new company logo and I want a new business card design. I dont know if the logo file i attached is in the correct format or quality. We are a New York City Specialty construction Firm specializing in high risk out of the box projects. I want a simple and classy business card that people will his card is as crisp as the work his company does.

Target Market(s)

Clients in the heavy construction industry in New York City

Industry/Entity Type

Construction Company

Contact Information for Business Card

Simple Classy - DIFFERENT

Font styles to use
Other font styles liked:
• Mach the logo font in some way

Colors

Designer to choose colors to be used in the design.

Requirements
Must have
• Uniqueness
Nice to have
• Nothing particular - Just different and classy - Timeless
Should not have
• Goofy Shit or Gimmicky shit

```html
<!DOCTYPE html>
<html lang="en">
<head>
<meta charset="utf-8">
<title>KVR Builders – Business Card</title>
<link href="https://fonts.googleapis.com/css2?family=Montserrat:wght@500;700;800&display=swap" rel="stylesheet">
<style>
  :root {
    --backdrop: #4a4a4a;
    --card-white: #ffffff;
    --card-black: #050505;
    --brand-blue: #1a8fd6;
    --rule-blue: #1f6fc0;
    --text-light: #f2f2f2;
    --wordmark: #1479c4;
  }
  * { box-sizing: border-box; margin: 0; padding: 0; }
  html, body {
    width: 1200px; height: 1000px; overflow: hidden;
    background: var(--backdrop);
    font-family: "Montserrat", sans-serif;
  }
  .canvas { position: relative; width: 1200px; height: 1000px; }
  .card {
    position: absolute; width: 620px; height: 354px;
    background: var(--card-white);
    box-shadow: 0 14px 30px rgba(0,0,0,.45);
    overflow: hidden;
  }
  .card--front { left: 150px; top: 100px; }
  .card--back { left: 480px; top: 540px; }

  .wordmark {
    position: absolute; display: flex; align-items: center; gap: 12px;
    font-weight: 800; color: var(--wordmark);
    letter-spacing: 1px; white-space: nowrap;
  }
  .wordmark__square { background: var(--wordmark); flex: none; }
  .card--front .wordmark { left: 50%; top: 50%; transform: translate(-50%, -50%); font-size: 46px; }
  .card--front .wordmark__square { width: 30px; height: 30px; }
  .card--back .wordmark { left: 200px; top: 80px; font-size: 32px; }
  .card--back .wordmark__square { width: 22px; height: 22px; }

  .back__rule {
    position: absolute; left: 0; right: 0; top: 188px; height: 5px;
    background: var(--rule-blue);
  }
  .back__panel {
    position: absolute; left: 0; right: 0; top: 196px; bottom: 0;
    background: var(--card-black);
  }
  .holder-name {
    position: absolute; left: 50px; top: 224px;
    font-weight: 700; font-size: 19px; letter-spacing: 1px;
    color: var(--brand-blue); text-transform: uppercase;
  }
  .contact {
    position: absolute; left: 420px; top: 210px;
    list-style: none; color: var(--text-light);
    font-weight: 500; font-size: 13px; line-height: 17px;
  }
  .contact__item { display: flex; align-items: flex-start; gap: 9px; }
  .contact__item--address { margin-bottom: 14px; }
  .contact__icon { width: 11px; height: 11px; margin-top: 3px; flex: none; fill: var(--brand-blue); }
</style>
</head>
<body>
<div class="canvas">

  <section class="card card--front" aria-label="Card front">
    <div class="wordmark"><span class="wordmark__square"></span>KVR BUILDERS, INC.</div>
  </section>

  <section class="card card--back" aria-label="Card back">
    <div class="wordmark"><span class="wordmark__square"></span>KVR BUILDERS, INC.</div>
    <div class="back__rule"></div>
    <div class="back__panel"></div>
    <p class="holder-name">Marco T. Bellini</p>
    <ul class="contact">
      <li class="contact__item contact__item--address">
        <svg class="contact__icon" viewBox="0 0 12 12"><path d="M6 0a4 4 0 0 0-4 4c0 3 4 8 4 8s4-5 4-8a4 4 0 0 0-4-4zm0 5.5A1.5 1.5 0 1 1 6 2.5a1.5 1.5 0 0 1 0 3z"/></svg>
        <span>412 River Dock Road -<br>Linden, New Jersey 07036</span>
      </li>
      <li class="contact__item">
        <svg class="contact__icon" viewBox="0 0 12 12"><path d="M2.5 0.5l2 2.5-1 1.5c.8 1.6 2.2 3 3.8 3.8l1.5-1 2.5 2-1.2 2.2C5 11 1 7 0.3 1.7z"/></svg>
        <span>908-555-0142</span>
      </li>
      <li class="contact__item">
        <svg class="contact__icon" viewBox="0 0 12 12"><path d="M3 0h6v12H3zm1 1.5v8h4v-8z"/></svg>
        <span>917-555-0187</span>
      </li>
      <li class="contact__item">
        <svg class="contact__icon" viewBox="0 0 12 12"><path d="M0 2h12v8H0zm1 1l5 3.5L11 3z"/></svg>
        <span>marco@kvrbuild.com</span>
      </li>
      <li class="contact__item">
        <svg class="contact__icon" viewBox="0 0 12 12"><circle cx="6" cy="6" r="6"/></svg>
        <span>www.kvrbuild.com</span>
      </li>
    </ul>
  </section>

</div>
</body>
</html>
```